Re design current site.

Redesign of the current site. Like current design But I don't own it so I need a custom design similar to the current one. Want the model pictures to be shown off as they currently do on the home page I want to show off contact info make it very noticeable and readable.
Target Market(s)
Males age 30-60
Number of Pages Required
1 page
Requirements
Must have
- Must show off model pictures on the page. Must show contact info easy to read easy to find.

```html
<!DOCTYPE html>
<html lang="en">
<head>
<meta charset="utf-8">
<title>Vela Models</title>
<link rel="stylesheet" href="https://fonts.googleapis.com/css2?family=Play:wght@400;700&family=Lato:wght@400;700&display=swap">
<style>
:root{
  --red:#e8202a;
  --black:#0c0c0c;
  --nav:#262626;
  --dark:#1b1b1b;
  --ink:#1d1d1d;
  --text:#3a3a3a;
  --muted:#777;
  --line:#d9d9d9;
  --soft:#f2f2f2;
  --white:#fff;
}
*{box-sizing:border-box;margin:0;padding:0}
html,body{width:1200px;height:2799px;overflow:hidden}
body{position:relative;background:var(--white);font-family:"Lato",sans-serif;color:var(--text)}
.abs{position:absolute}
.display{font-family:"Play",sans-serif}

/* header */
.site-header{position:absolute;left:0;top:0;width:1200px;height:129px;background:var(--black)}
.brand{position:absolute;left:99px;top:38px;display:flex;align-items:center;gap:14px}
.brand-mark{width:40px;height:40px;border-radius:50%;background:var(--red)}
.brand-name{font-family:"Play",sans-serif;font-size:36px;font-weight:400;color:var(--white);letter-spacing:1px}
.contact-item{position:absolute;top:42px;display:flex;align-items:center;gap:14px;color:var(--white);font-family:"Play",sans-serif;font-weight:700}
.contact-item .ico{width:38px;height:38px;border-radius:50%;background:var(--red);display:flex;align-items:center;justify-content:center}
.contact-phone{left:610px;font-size:20px}
.contact-mail{left:840px;font-size:17px}
.contact-divider{position:absolute;left:818px;top:50px;width:1px;height:22px;background:#555}

/* nav */
.main-nav{position:absolute;left:0;top:129px;width:1200px;height:43px;background:var(--nav);border-top:1px solid #333}
.main-nav ul{list-style:none;position:absolute;left:99px;top:0;display:flex;height:43px}
.main-nav li{height:43px;display:flex;align-items:center;justify-content:center;font-family:"Play",sans-serif;font-weight:700;font-size:13px;color:var(--white);text-transform:uppercase;border-right:1px solid #3b3b3b}
.main-nav li.active{background:var(--red)}

/* hero */
.hero{position:absolute;left:0;top:172px;width:1200px;height:257px;background:linear-gradient(90deg,#b99a84 0%,#d8cbc0 30%,#cfc8c0 55%,#b6aca2 100%)}
.hero-tagline{position:absolute;right:99px;top:64px;text-align:right;font-family:"Play",sans-serif;font-weight:700;font-size:33px;line-height:40px;color:var(--ink);text-transform:uppercase}
.hero-strip{position:absolute;left:0;bottom:0;width:1200px;height:56px;background:rgba(20,20,20,.78);display:flex;align-items:center;justify-content:center;font-family:"Play",sans-serif;font-weight:700;font-size:24px;color:var(--white)}

/* section headings */
.section-title{position:absolute;left:0;width:1200px;text-align:center;font-family:"Play",sans-serif;font-weight:700;font-size:31px;color:var(--ink);text-transform:uppercase}
.section-title span{color:var(--red)}
.title-rule{position:absolute;left:278px;width:644px;height:1px;background:var(--line)}
.title-rule::after{content:"";position:absolute;left:290px;top:-1px;width:64px;height:3px;background:#333}

/* model cards */
.model-card{position:absolute;width:233px;height:341px;background:var(--white);border:1px solid #e4e4e4;box-shadow:0 1px 3px rgba(0,0,0,.08)}
.model-photo{position:absolute;left:0;top:0;width:231px;height:246px}
.model-plus{position:absolute;left:96px;top:226px;width:40px;height:40px;border-radius:50%;background:#222;display:flex;align-items:center;justify-content:center}
.model-plus.active{background:var(--red)}
.model-name{position:absolute;left:0;top:276px;width:231px;text-align:center;font-family:"Play",sans-serif;font-weight:700;font-size:19px;color:var(--ink)}
.model-stats{position:absolute;left:0;top:306px;width:231px;text-align:center;font-size:13px;color:#444}
.btn-dark{position:absolute;background:#222;color:var(--white);font-family:"Play",sans-serif;font-weight:700;font-size:14px;text-transform:uppercase;display:flex;align-items:center;justify-content:center}

/* about */
.about{position:absolute;left:0;top:1388px;width:1200px;height:549px;background:var(--soft)}
.about-title{position:absolute;left:99px;top:38px;font-family:"Play",sans-serif;font-weight:700;font-size:31px;color:var(--ink);text-transform:uppercase}
.about-title span{color:var(--red)}
.about-rule{position:absolute;left:99px;top:90px;width:647px;height:1px;background:var(--line)}
.about-body{position:absolute;left:99px;top:114px;width:650px;font-size:14.5px;line-height:24px;color:#333}
.about-body p{margin-bottom:10px}
.about-body .lead{font-weight:700;font-size:16px;color:var(--ink);margin-bottom:6px}

.booking{position:absolute;left:797px;top:53px;width:304px;height:447px;background:var(--white);box-shadow:0 6px 14px rgba(0,0,0,.18)}
.booking-head{height:56px;background:var(--red);color:var(--white);font-family:"Play",sans-serif;font-weight:700;font-size:21px;display:flex;align-items:center;justify-content:center;text-transform:uppercase}
.booking-intro{padding:16px 22px 0;font-size:12px;line-height:20px;color:#555}
.field{position:absolute;left:22px;width:260px;height:38px;border:1px solid #e2e2e2;background:#fafafa;font-size:11.5px;color:#777;display:flex;align-items:center;padding:0 14px;justify-content:space-between}
.booking .btn-dark{left:22px;width:260px;height:38px;top:382px;font-size:15px}

/* rates */
.rates-intro{position:absolute;left:180px;top:2062px;width:840px;text-align:center;font-size:14px;line-height:26px;color:#333}
.rates-table{position:absolute;left:220px;top:2133px;width:760px;border-collapse:collapse;font-family:"Play",sans-serif}
.rates-table th{background:#2b2b2b;color:var(--white);font-size:25px;font-weight:700;text-align:left;height:64px;padding-left:38px;border-right:1px solid #444}
.rates-table td{font-size:19px;color:#444;height:48px;padding-left:38px;border:1px solid #e3e3e3}
.rates-table tr:nth-child(even) td{background:#f6f6f6}

/* footer */
.site-footer{position:absolute;left:0;top:2450px;width:1200px;height:297px;background:var(--dark)}
.footer-cta{position:absolute;left:386px;top:2443px;width:428px;height:65px;background:var(--red);color:var(--white);font-family:"Play",sans-serif;font-weight:700;font-size:29px;display:flex;align-items:center;justify-content:center;box-shadow:0 3px 8px rgba(0,0,0,.4)}
.footer-col{position:absolute;top:2550px}
.footer-head{font-family:"Play",sans-serif;font-weight:700;font-size:18px;color:var(--white);text-transform:uppercase;padding-bottom:10px;border-bottom:1px solid #555;width:170px}
.footer-head::after{content:"";display:block;width:50px;height:2px;background:var(--red);position:relative;top:11px}
.footer-links{display:grid;grid-template-columns:86px 86px;row-gap:9px;margin-top:24px;font-size:13px;color:#ddd}
.footer-org{margin-top:26px;font-family:"Play",sans-serif;font-weight:700;font-size:15px;color:var(--white)}
.footer-line{display:flex;align-items:center;gap:14px;margin-top:14px;font-size:13px;color:#ddd}
.newsletter-copy{margin-top:26px;font-size:12px;line-height:18px;color:#ddd;width:160px}
.newsletter-form{display:flex;margin-top:22px}
.newsletter-input{width:166px;height:32px;background:var(--white);font-size:11px;color:#777;display:flex;align-items:center;gap:8px;padding-left:10px}
.newsletter-btn{width:100px;height:32px;background:var(--red);color:var(--white);font-family:"Play",sans-serif;font-weight:700;font-size:12px;display:flex;align-items:center;justify-content:center}
.listing-badge{position:absolute;left:954px;top:2572px;width:147px;height:126px;background:#d9d4bc;border:2px solid #efefe6}
.bottom-bar{position:absolute;left:0;top:2747px;width:1200px;height:52px;background:var(--black);color:#ddd;font-size:14px;display:flex;align-items:center;justify-content:center}
</style>
</head>
<body>

<header class="site-header">
  <div class="brand"><span class="brand-mark"></span><span class="brand-name">VELA MODELS</span></div>
  <div class="contact-item contact-phone">
    <span class="ico"><svg width="18" height="18" viewBox="0 0 24 24"><path fill="#fff" d="M6.6 10.8a15 15 0 0 0 6.6 6.6l2.2-2.2c.3-.3.7-.4 1-.2 1.1.4 2.3.6 3.6.6.6 0 1 .4 1 1V20c0 .6-.4 1-1 1A17 17 0 0 1 3 4c0-.6.4-1 1-1h3.5c.6 0 1 .4 1 1 0 1.3.2 2.5.6 3.6.1.3 0 .7-.2 1z"/></svg></span>
    555-010-4821
  </div>
  <span class="contact-divider"></span>
  <div class="contact-item contact-mail">
    <span class="ico"><svg width="18" height="14" viewBox="0 0 24 18"><rect x="1" y="1" width="22" height="16" rx="2" fill="#fff"/><path d="M2 2l10 8 10-8" fill="none" stroke="#e8202a" stroke-width="2"/></svg></span>
    hello@velamodels.example
  </div>
</header>

<nav class="main-nav">
  <ul>
    <li class="active" style="width:124px">Home</li>
    <li style="width:156px">About Us</li>
    <li style="width:146px">Booking</li>
    <li style="width:146px">Models</li>
    <li style="width:128px">Rates</li>
    <li style="width:172px">Employment</li>
    <li style="width:130px">Links</li>
  </ul>
</nav>

<section class="hero" role="img" aria-label="Banner photo of a woman in a white top lounging on a bed">
  <div class="hero-tagline">Treat yourself and<br>we'll treat you</div>
  <div class="hero-strip">Please Contact Us About Additional Models Not Posted Publicly!</div>
</section>

<h2 class="section-title" style="top:472px">Our <span>Models</span></h2>
<div class="title-rule" style="top:524px"></div>

<article class="model-card" style="left:99px;top:554px">
  <div class="model-photo" role="img" aria-label="Photo of model Lena" style="background:linear-gradient(135deg,#d8b9a8,#c0457e 60%,#8a6b63)"></div>
  <span class="model-plus active"><svg width="14" height="14"><path d="M7 1v12M1 7h12" stroke="#fff" stroke-width="2.4"/></svg></span>
  <h3 class="model-name">Lena</h3><p class="model-stats">20 - 5'3 - 120 - 34B</p>
</article>
<article class="model-card" style="left:355px;top:554px">
  <div class="model-photo" role="img" aria-label="Photo of model Marisa" style="background:linear-gradient(135deg,#e7ddd3,#b98a6a 55%,#6d4a36)"></div>
  <span class="model-plus"><svg width="14" height="14"><path d="M7 1v12M1 7h12" stroke="#fff" stroke-width="2.4"/></svg></span>
  <h3 class="model-name">Marisa</h3><p class="model-stats">23 - 5'0 - 110 - 34C</p>
</article>
<article class="model-card" style="left:612px;top:554px">
  <div class="model-photo" role="img" aria-label="Photo of model Nora Vale" style="background:linear-gradient(135deg,#4f6e2c,#7f9a4a 50%,#3d5322)"></div>
  <span class="model-plus"><svg width="14" height="14"><path d="M7 1v12M1 7h12" stroke="#fff" stroke-width="2.4"/></svg></span>
  <h3 class="model-name">Nora Vale</h3><p class="model-stats">23 - 5'6 - 110 - 32B</p>
</article>
<article class="model-card" style="left:870px;top:554px">
  <div class="model-photo" role="img" aria-label="Photo of model Quinn" style="background:linear-gradient(135deg,#cdbfae,#7a5a44 55%,#3b2c22)"></div>
  <span class="model-plus"><svg width="14" height="14"><path d="M7 1v12M1 7h12" stroke="#fff" stroke-width="2.4"/></svg></span>
  <h3 class="model-name">Quinn</h3><p class="model-stats">21 - 5'5 - 110 - 32C</p>
</article>

<article class="model-card" style="left:99px;top:922px">
  <div class="model-photo" role="img" aria-label="Photo of model Celeste" style="background:linear-gradient(135deg,#3a2a28,#9a5a5e 50%,#c14e88)"></div>
  <span class="model-plus"><svg width="14" height="14"><path d="M7 1v12M1 7h12" stroke="#fff" stroke-width="2.4"/></svg></span>
  <h3 class="model-name">Celeste</h3><p class="model-stats">21 - 5'4 - 130 - 34C</p>
</article>
<article class="model-card" style="left:355px;top:922px">
  <div class="model-photo" role="img" aria-label="Photo of model Dana Rivers" style="background:linear-gradient(135deg,#141010,#3a1c1c 55%,#111)"></div>
  <span class="model-plus"><svg width="14" height="14"><path d="M7 1v12M1 7h12" stroke="#fff" stroke-width="2.4"/></svg></span>
  <h3 class="model-name">Dana Rivers MO</h3><p class="model-stats">20 - 5'1 - 90 - 34B</p>
</article>
<article class="model-card" style="left:612px;top:922px">
  <div class="model-photo" role="img" aria-label="Photo of model Tessa" style="background:linear-gradient(135deg,#d6d3cc,#8c7468 55%,#3c302c)"></div>
  <span class="model-plus"><svg width="14" height="14"><path d="M7 1v12M1 7h12" stroke="#fff" stroke-width="2.4"/></svg></span>
  <h3 class="model-name">Tessa</h3><p class="model-stats">22 - 5'1 - 95 - 34A</p>
</article>
<article class="model-card" style="left:870px;top:922px">
  <div class="model-photo" role="img" aria-label="Photo of model Jolie" style="background:linear-gradient(135deg,#e2cfb8,#b88a5e 55%,#8a5a34)"></div>
  <span class="model-plus"><svg width="14" height="14"><path d="M7 1v12M1 7h12" stroke="#fff" stroke-width="2.4"/></svg></span>
  <h3 class="model-name">Jolie</h3><p class="model-stats">21 - 5'3 - 115 - 32B</p>
</article>

<div class="btn-dark" style="left:517px;top:1299px;width:166px;height:37px">View All Models</div>

<section class="about">
  <h2 class="about-title">About <span>Vela Models</span></h2>
  <div class="about-rule"></div>
  <div class="about-body">
    <p class="lead" style="margin-bottom:4px">Male &amp; female couple available as well.</p>
    <p class="lead">Custom clips and videos available for sale!</p>
    <p><strong>VelaModels Concierge Service</strong> allows clients to request VelaModels to search for models in the location you plan on traveling to. We will search and find attractive models for the dates requested. We also verify they are interested in the service you expect/request and that the pictures we have are recent and real.</p>
    <p>Are you looking for the best Miami Escort Services providing incall and outcall serving the Miami, Fort Lauderdale, West Palm Beach &amp; other major city's? If so, then you have come to the right place! With the most beautiful, hot, sexy and sizzling companions in the Miami, Fort Lauderdale &amp; West Palm Beach areas. Click Here to See Our Models!</p>
    <p>we, at VelaModels Escorts, can accommodate your dreams &amp; demands for any and all kinds of engagements. Our main goal is to offer you a fully satisfying, warm, and pleasurable...</p>
  </div>
  <div class="btn-dark" style="left:99px;top:461px;width:123px;height:38px">Read More</div>

  <aside class="booking">
    <div class="booking-head">Bookings</div>
    <p class="booking-intro">Experience our exemplary service for yourself. Once you book with us, you'll be hooked.</p>
    <div class="field" style="top:128px">Choose a Model...<svg width="10" height="6"><path d="M1 1l4 4 4-4" fill="none" stroke="#999" stroke-width="1.5"/></svg></div>
    <div class="field" style="top:175px">Full Name</div>
    <div class="field" style="top:222px">Email</div>
    <div class="field" style="top:269px">Phone</div>
    <div class="field" style="top:316px">Appointment Date<svg width="12" height="12"><rect x="1" y="2" width="10" height="9" fill="none" stroke="#aaa"/><path d="M1 5h10" stroke="#aaa"/></svg></div>
    <div class="btn-dark">Next Step</div>
  </aside>
</section>

<h2 class="section-title" style="top:1980px">Rates</h2>
<div class="title-rule" style="top:2033px"></div>
<p class="rates-intro">We're so glad you're interested in meeting with one of our upscale companions. Here are the donations we request for your entertainment. These rates are non-negotiable.</p>
<table class="rates-table">
  <tr><th style="width:254px">Time</th><th style="width:252px">Incall</th><th>Outcall</th></tr>
  <tr><td>1 HR</td><td>N/A</td><td>$360</td></tr>
  <tr><td>2 HR</td><td>N/A</td><td>$660</td></tr>
  <tr><td>3 HR</td><td>N/A</td><td>$900</td></tr>
  <tr><td>Over Night</td><td>N/A</td><td>$1,900</td></tr>
</table>

<footer class="site-footer"></footer>
<div class="footer-cta">Contact Us - 555-010-4821</div>

<div class="footer-col" style="left:99px">
  <h4 class="footer-head">Quick Links</h4>
  <div class="footer-links"><span>Home</span><span>Rates</span><span>About Us</span><span>Employment</span><span>Booking</span><span>Links</span><span>Models</span></div>
</div>
<div class="footer-col" style="left:355px">
  <h4 class="footer-head">Contact Info</h4>
  <p class="footer-org">VELA MODELS</p>
  <p class="footer-line"><svg width="14" height="14" viewBox="0 0 24 24"><path fill="#e8202a" d="M6.6 10.8a15 15 0 0 0 6.6 6.6l2.2-2.2c.3-.3.7-.4 1-.2 1.1.4 2.3.6 3.6.6.6 0 1 .4 1 1V20c0 .6-.4 1-1 1A17 17 0 0 1 3 4c0-.6.4-1 1-1h3.5c.6 0 1 .4 1 1 0 1.3.2 2.5.6 3.6.1.3 0 .7-.2 1z"/></svg>555-010-4821</p>
  <p class="footer-line"><svg width="14" height="11" viewBox="0 0 24 18"><rect x="1" y="1" width="22" height="16" rx="2" fill="#e8202a"/><path d="M2 2l10 8 10-8" fill="none" stroke="#1b1b1b" stroke-width="2"/></svg>hello@velamodels.example</p>
</div>
<div class="footer-col" style="left:595px">
  <h4 class="footer-head" style="width:240px">Join My Newsletter</h4>
  <p class="newsletter-copy">Get The Latest Updates By Entering Your Email Address</p>
  <div class="newsletter-form">
    <div class="newsletter-input"><svg width="12" height="9" viewBox="0 0 24 18"><rect x="1" y="1" width="22" height="16" fill="#bbb"/></svg>Email Address</div>
    <div class="newsletter-btn">SUBSCRIBE</div>
  </div>
</div>
<div class="listing-badge" role="img" aria-label="Review listing badge"></div>

<div class="bottom-bar">Copyright © 2017 Vela Models. All Right Reserved</div>

</body>
</html>
```